Not-for-profit Community Law Business Card

Not-for-Profit community law firm are looking for new business card design to accompany a new logo.
The cards are to assist the organisation in reaching their strategic objective of generating greater networking amongst the community; specifically with other service providers, clients, and community influencers.
It should stand out. Be professional, strong, creative, clear in detail. The logo should be a major feature of the design.
Updates

Hi All,

Thank you for the submissions so far. I have uploaded the logo and colour details again, as requested. If you have any further issues downloading them or need a different format please contact me on rosa_pellin@vtq.example.au

Kind regards,

Industry/Entity Type

Law Firm

Requirements
Must have
• Logo (attached)
Person's name
Position
Phone
Fax
Email
PO Box address
Website
Colours from the logo.

```html
<!DOCTYPE html>
<html lang="en">
<head>
<meta charset="utf-8">
<title>Harbour Point Legal Centre – Business Card</title>
<link rel="stylesheet" href="https://fonts.googleapis.com/css2?family=Maven+Pro:wght@400;500;700&display=swap">
<style>
  :root {
    --stage: #e9e6e1;
    --brand-blue: #2a85cc;
    --brand-navy: #33338a;
    --card-white: #fbfbfb;
    --ink: #2e2e2e;
    --ink-soft: #3c3c3c;
    --white: #ffffff;
  }
  * { margin: 0; padding: 0; box-sizing: border-box; }
  html, body {
    width: 1200px; height: 900px; overflow: hidden;
    background: var(--stage);
    font-family: "Maven Pro", sans-serif;
  }
  .stage {
    position: relative; width: 1200px; height: 900px;
    display: flex; flex-direction: column; align-items: center; justify-content: center;
    gap: 44px;
  }
  .card {
    width: 660px; height: 380px;
    box-shadow: 0 6px 18px rgba(0,0,0,0.18);
    position: relative;
  }
  .card--front { background: var(--brand-blue); }
  .card--back { background: var(--card-white); }

  .brand {
    position: absolute; display: flex; align-items: center; gap: 14px;
  }
  .brand__dot {
    width: 58px; height: 58px; border-radius: 50%; flex: none;
  }
  .brand__name {
    font-weight: 500; font-size: 30px; line-height: 1.05; letter-spacing: 0.5px;
  }
  .card--front .brand { left: 130px; top: 150px; }
  .card--front .brand__dot { background: var(--white); }
  .card--front .brand__name { color: var(--white); }

  .card--back .brand { left: 150px; top: 40px; }
  .card--back .brand__dot { background: var(--brand-blue); }
  .card--back .brand__name { color: var(--brand-blue); }

  .contact { position: absolute; left: 80px; top: 160px; color: var(--ink-soft); }
  .contact__person {
    font-size: 27px; font-weight: 400; letter-spacing: 1px; color: var(--ink);
    text-transform: uppercase; margin-bottom: 16px;
  }
  .contact__role { font-size: 19px; letter-spacing: 1.5px; }
  .contact__line { font-size: 18px; line-height: 1.3; letter-spacing: 0.4px; }
  .contact__label { color: var(--brand-navy); font-weight: 700; margin-right: 4px; }
  .contact__gap { margin-left: 12px; }
  .contact__address { font-size: 19px; margin-top: 8px; letter-spacing: 0.4px; }
  .contact__web {
    font-size: 19px; font-weight: 700; color: var(--brand-navy);
    margin-top: 14px; letter-spacing: 0.6px;
  }
</style>
</head>
<body>
<main class="stage">
  <section class="card card--front" aria-label="Card front">
    <div class="brand">
      <span class="brand__dot"></span>
      <span class="brand__name">Harbour Point<br>Legal Centre Inc.</span>
    </div>
  </section>

  <section class="card card--back" aria-label="Card back">
    <div class="brand">
      <span class="brand__dot"></span>
      <span class="brand__name">Harbour Point<br>Legal Centre Inc.</span>
    </div>
    <div class="contact">
      <p class="contact__person">Maren Ashdown | <span class="contact__role">Manager</span></p>
      <p class="contact__line"><span class="contact__label">t</span> 555.210.0184<span class="contact__gap"><span class="contact__label">f</span> 555.210.0192</span></p>
      <p class="contact__line"><span class="contact__label">e</span> mashdown@harbourpointlegal.org</p>
      <p class="contact__address">4120 Quayside Road, Ste. 200, Lakewood, TX 75201</p>
      <p class="contact__web">www.harbourpointlegal.org</p>
    </div>
  </section>
</main>
</body>
</html>
```